wealth management firm, professional group, new model

we have a logo that works but we need a card, white background using our colors...clean look

our tag line if can be used in

The Bridge From Client to Owner

```html
<!DOCTYPE html>
<html lang="en">
<head>
<meta charset="utf-8">
<title>Arcway Wealth Partners – Business Card</title>
<link href="https://fonts.googleapis.com/css2?family=Open+Sans:wght@400;700&display=swap" rel="stylesheet">
<style>
  :root {
    --backdrop: #2a2a2a;
    --card-dark: #1d1d1e;
    --card-light: #ffffff;
    --navy: #1f2d52;
    --ink-grey: #5a5a5a;
    --rule-grey: #9a9a9a;
    --soft-white: #e8e8e8;
  }
  * { box-sizing: border-box; margin: 0; padding: 0; }
  html, body {
    width: 1200px; height: 900px; overflow: hidden;
    background: var(--backdrop);
  }
  .stage {
    width: 1200px; height: 900px;
    display: flex; flex-direction: column; align-items: center; justify-content: center;
    gap: 48px;
  }
  .card {
    width: 640px; height: 366px;
    border-radius: 18px;
    position: relative;
    box-shadow: 0 10px 30px rgba(0,0,0,.45);
    font-family: "Open Sans", sans-serif;
  }

  /* Company name set as plain text */
  .company-name {
    font-family: "Open Sans", sans-serif;
    font-weight: 400;
    letter-spacing: 0;
    line-height: 1.15;
  }

  /* Back side */
  .card--back { background: var(--card-dark); }
  .card--back .company-name {
    position: absolute; left: 0; right: 0; top: 112px;
    text-align: center;
    font-size: 40px;
    color: var(--soft-white);
  }
  .tagline {
    position: absolute; left: 0; right: 0; bottom: 62px;
    text-align: center;
    font-size: 20px;
    color: var(--soft-white);
  }

  /* Front side */
  .card--front { background: var(--card-light); }
  .card--front .company-name {
    position: absolute; left: 30px; top: 120px; width: 270px;
    text-align: center;
    font-size: 30px;
    color: var(--navy);
  }
  .divider {
    position: absolute; left: 318px; top: 92px; width: 1px; height: 140px;
    background: var(--rule-grey);
  }
  .contact {
    position: absolute; left: 340px; top: 92px;
    color: var(--ink-grey);
  }
  .contact__name {
    font-weight: 700; font-size: 24px; color: var(--navy); letter-spacing: 0.02em; line-height: 1.1;
  }
  .contact__role { font-size: 17px; margin-bottom: 10px; }
  .contact__list { list-style: none; }
  .contact__item {
    display: flex; align-items: center; gap: 8px;
    font-size: 18px; line-height: 1.4;
  }
  .contact__item svg { width: 14px; height: 14px; fill: var(--ink-grey); flex: none; }
  .address {
    position: absolute; left: 0; right: 0; bottom: 52px;
    text-align: center;
    font-size: 20px; color: var(--ink-grey);
  }
</style>
</head>
<body>
<main class="stage">
  <section class="card card--back" aria-label="Card back">
    <p class="company-name">Arcway Wealth Partners</p>
    <p class="tagline">The Bridge From Client to Owner</p>
  </section>

  <section class="card card--front" aria-label="Card front">
    <p class="company-name">Arcway<br>Wealth Partners</p>
    <div class="divider"></div>
    <div class="contact">
      <p class="contact__name">DANIEL MOORE</p>
      <p class="contact__role">Managing Director</p>
      <ul class="contact__list">
        <li class="contact__item">
          <svg viewBox="0 0 16 16" aria-hidden="true"><path d="M2 5c0-2 2-3 6-3s6 1 6 3v1h-3V5H5v1H2zM4 7h8l2 7H2z"/></svg>
          044-123 456 789
        </li>
        <li class="contact__item">
          <svg viewBox="0 0 16 16" aria-hidden="true"><path d="M1 3h14v10H1zM2 4l6 5 6-5v-.2H2z" fill-rule="evenodd"/></svg>
          info@webname.com
        </li>
        <li class="contact__item">
          <svg viewBox="0 0 16 16" aria-hidden="true"><circle cx="8" cy="8" r="7"/></svg>
          www.websitename.com
        </li>
      </ul>
    </div>
    <p class="address">Your Address, City, State, Zip 0000</p>
  </section>
</main>
</body>
</html>
```